Business Cards and Stationery for Consulting Firm
Meridian Stone Partners
Business Cards and Stationery for Consulting Firm - Consulting
Creative Brief
Professional
Leo Farrow, PE, LEED AP
President
2786 Harlow St Kensington, MD 20817
leo.farrow@meridianstonepartners.example
www.meridianstonepartners.example
We want a black background with only the logo. We want the logo to have a metallic finish on the back side only.
mspadmin mspadmin
Please make sure to use image file "31 MSP Revision" on the back of the business card, because we want the back of the business card to have a black background. Use image file "21 MSP Revision" when working with a white background.

```html
<!DOCTYPE html>
<html lang="en">
<head>
<meta charset="utf-8">
<title>Meridian Stone Partners — Business Cards</title>
<link rel="stylesheet" href="https://fonts.googleapis.com/css2?family=Montserrat:wght@400;600;800&display=swap">
<style>
  :root {
    --backdrop: #d9d9d9;
    --card-white: #ffffff;
    --card-black: #0b0b0b;
    --ink: #1a1a1a;
    --ink-soft: #444444;
    --muted: #6e6e6e;
    --rule: #9a9a9a;
    --band: #111111;
    --band-text: #e6e6e6;
    --mark-grey: #5a5a5a;
  }
  * { box-sizing: border-box; margin: 0; padding: 0; }
  html, body {
    width: 1200px; height: 901px; overflow: hidden;
    background: var(--backdrop);
    font-family: "Montserrat", sans-serif;
  }
  .canvas { position: relative; width: 1200px; height: 901px; }

  .card {
    position: absolute;
    width: 560px; height: 320px;
    border-radius: 14px;
    overflow: hidden;
    box-shadow: 0 10px 24px rgba(0,0,0,0.25);
  }

  /* Back side */
  .card-back {
    left: 70px; top: 90px;
    background: radial-gradient(ellipse at 40% 30%, #2a2a2a 0%, var(--card-black) 70%);
  }
  .card-back .wordmark {
    position: absolute; left: 0; right: 0; top: 128px;
    text-align: center;
    font-weight: 800; font-size: 52px; letter-spacing: 2px;
    color: var(--mark-grey);
  }

  /* Front side */
  .card-front {
    left: 570px; top: 490px;
    background: var(--card-white);
  }
  .brand {
    position: absolute; left: 0; right: 0; top: 46px;
    text-align: center;
  }
  .brand-mark {
    font-weight: 800; font-size: 46px; letter-spacing: 2px;
    color: var(--ink); line-height: 1;
  }
  .brand-name {
    margin-top: 6px;
    font-weight: 800; font-size: 14px; letter-spacing: 0.5px;
    color: var(--ink);
  }
  .person {
    position: absolute; right: 290px; top: 160px;
    text-align: right;
  }
  .person-name { font-size: 14px; color: var(--ink); }
  .person-title { margin-top: 4px; font-size: 11px; color: var(--muted); }
  .divider {
    position: absolute; left: 280px; top: 156px;
    width: 1px; height: 82px; background: var(--rule);
  }
  .contact {
    position: absolute; left: 292px; top: 160px;
    font-size: 10.5px; color: var(--ink-soft); line-height: 1.45;
  }
  .contact-line { display: flex; align-items: center; gap: 6px; margin-top: 5px; }
  .contact-line svg { flex: none; }
  .contact .email { font-size: 9.5px; }
  .band {
    position: absolute; left: 0; right: 0; bottom: 0; height: 50px;
    background: var(--band);
    display: flex; align-items: center; justify-content: center;
  }
  .band::before {
    content: ""; position: absolute; left: 0; right: 0; top: -6px;
    height: 2px; background: var(--rule);
  }
  .website {
    font-size: 11px; letter-spacing: 2px; color: var(--band-text);
  }
</style>
</head>
<body>
<main class="canvas">

  <section class="card card-back" aria-label="Card back">
    <div class="wordmark">MSP</div>
  </section>

  <section class="card card-front" aria-label="Card front">
    <div class="brand">
      <div class="brand-mark">MSP</div>
      <div class="brand-name">MERIDIAN STONE PARTNERS</div>
    </div>

    <div class="person">
      <div class="person-name">Leo Farrow, PE, LEED AP</div>
      <div class="person-title">President</div>
    </div>

    <div class="divider"></div>

    <div class="contact">
      <div>2786 Harlow St</div>
      <div>Kensington, MD 20817</div>
      <div class="contact-line">
        <svg width="9" height="12" viewBox="0 0 9 12" aria-hidden="true">
          <rect x="0.5" y="0.5" width="8" height="11" rx="1.5" fill="none" stroke="#333" stroke-width="1"/>
          <rect x="3" y="9.3" width="3" height="1" fill="#333"/>
        </svg>
        <span>954-555-0148</span>
      </div>
      <div class="contact-line">
        <svg width="11" height="8" viewBox="0 0 11 8" aria-hidden="true">
          <rect x="0" y="0" width="11" height="8" rx="1" fill="#333"/>
          <path d="M0.5 0.8 L5.5 4.6 L10.5 0.8" fill="none" stroke="#fff" stroke-width="0.9"/>
        </svg>
        <span class="email">leo.farrow@meridianstonepartners.example</span>
      </div>
    </div>

    <div class="band">
      <span class="website">www.meridianstonepartners.example</span>
    </div>
  </section>

</main>
</body>
</html>
```